Broschüre
Zielgruppe
Firmen und Privatpersonen
Unsere Zielkunden sind im bereich Firmen
Firmen die etwas für die Umwelt tun wollen oder sich einen Grünen anstrich geben wollen
Privatpersonen hier ist es die Gruppe die sich für den erhalt der Natur einsetzten die Bienen oder Naturprojekte unterstützen wollen und dergleichen. In der regel Menschen die BIO Kaufen
Aufgabenstellung
Standard Falzflyer DIN-A4 4 Seiten / Logo vorhanden / Unbedingt noch ein Freifeld zum ausfüllen zum bestellen. Daten die wir zum bestellen benötigen Name/Adresse/Telefonnummer/E-Mail/Unterschrift

```html
<!DOCTYPE html>
<html lang="de">
<head>
<meta charset="utf-8">
<title>Bienenpatenschaft – Falzflyer Innenseite</title>
<link href="https://fonts.googleapis.com/css2?family=Crimson+Text:ital,wght@0,400;0,600;0,700&family=Cormorant+Garamond:wght@500;600&display=swap" rel="stylesheet">
<style>
  :root{
    --bg:#b9b9b9;
    --paper:#ffffff;
    --honey:#f5ac1c;
    --gold:#e0ad0a;
    --brown:#6b3c08;
    --heading:#6a4210;
    --ink:#2b2118;
  }
  *{box-sizing:border-box;margin:0;padding:0}
  html,body{width:1200px;height:675px;overflow:hidden;background:var(--bg)}
  body{font-family:"Crimson Text",Georgia,serif;color:var(--ink)}
  .spread{position:absolute;left:143px;top:14px;width:914px;height:646px;background:var(--paper);overflow:hidden;box-shadow:0 6px 14px rgba(0,0,0,.35)}
  .abs{position:absolute}
  .photo{position:absolute}
  .photo--bees{left:0;top:236px;width:306px;height:410px;
    background:
      linear-gradient(180deg,rgba(255,255,255,1) 0%,rgba(255,255,255,0) 22%),
      linear-gradient(90deg,#7a4c10 0%,#b9781c 30%,#e7a940 60%,#f6d494 85%,#fff 100%);}
  .photo--flower{left:720px;top:18px;width:194px;height:126px;
    background:
      linear-gradient(90deg,#fff 0%,rgba(255,255,255,0) 35%),
      linear-gradient(180deg,rgba(255,255,255,0) 60%,#fff 100%),
      linear-gradient(120deg,#f3dcae 0%,#e9c27a 40%,#d9a3a0 70%,#c98a94 100%);}
  .photo--jars{left:470px;top:372px;width:444px;height:274px;
    background:
      linear-gradient(180deg,#fff 0%,rgba(255,255,255,0) 40%),
      linear-gradient(90deg,#fff 0%,rgba(255,255,255,0) 30%),
      linear-gradient(90deg,#f3d7a0 0%,#e6a33a 40%,#c8761a 65%,#e9b24e 85%,#f1c98a 100%);}
  .body{font-size:12px;line-height:13px;white-space:nowrap}
  .title-vision{left:17px;top:29px;font-weight:700;font-size:22px;color:#fff;letter-spacing:.5px}
  .col-left{left:17px;top:95px}
  .col-left p+p{margin-top:13px}
  .help{left:33px;top:288px;font-weight:700;font-size:20px;line-height:22px;color:var(--heading);border-bottom:2px solid var(--heading);padding-bottom:1px;white-space:nowrap}
  .col-mid{left:316px;top:52px}
  .indent{text-indent:15px}
  .col-mid .gap{margin-top:15px}
  .steps{left:329px;top:401px;list-style:none}
  .steps li{position:relative;padding-left:25px;height:39px;font-size:12px;line-height:13px;white-space:nowrap}
  .steps svg{position:absolute;left:0;top:4px}
  .serif-head{font-family:"Cormorant Garamond",Georgia,serif;font-weight:600;font-size:24px;line-height:25px;color:var(--heading)}
  .h-engage{left:615px;top:75px}
  .col-right{left:618px;top:138px}
  .rule{left:618px;top:244px;width:281px;height:1.5px;background:var(--ink)}
  .h-project{left:618px;top:257px}
  .lead{left:618px;top:318px;font-size:14px;line-height:16px;color:#1a140e;white-space:nowrap}
  .col-right2{left:618px;top:357px}
</style>
</head>
<body>
<main class="spread">
  <div class="photo photo--bees" role="img" aria-label="Foto: Honigbienen auf goldener Wabe"></div>
  <div class="photo photo--flower" role="img" aria-label="Foto: Biene an einer Blüte"></div>
  <div class="photo photo--jars" role="img" aria-label="Foto: Honiggläser, Pollen und Blüten"></div>

  <svg class="abs" style="left:0;top:0" width="914" height="646" viewBox="0 0 914 646" aria-hidden="true">
    <path d="M0 0H914V18C700 20 420 26 250 48C130 62 40 78 0 90Z" fill="var(--honey)"/>
    <path d="M480 646C650 628 820 600 914 560V646Z" fill="var(--honey)"/>
  </svg>

  <h1 class="abs title-vision">Die Vision ...</h1>
  <div class="abs body col-left">
    <p>... vom eigenen Honig, vom eigenen Bienenvolk &amp; vom<br>gemeinsamen Bienendorf. Wir lesen es in der Zeitung,<br>wir sehen Berichte im Fernsehen: Das Bienensterben nimmt<br>immer größere Ausmaße an und dies wird, für uns alle, ein<br>elementares Problem werden. Bienen gelten als die wich-<br>tigsten bestäubenden Insekten und ihr Fortbestand wird<br>durch weiter zunehmende Wetterkapriolen, abnehmende<br>Lebensräume (Monokulturen), Befall durch Parasiten<br>und vor allem durch den verstärkten Einsatz von Pestiziden<br>in der Landwirtschaft drastisch bedroht.</p>
    <p>Bienenhof Seewinkel hat sich nun diesem Thema<br>verschrieben. Wir müssen diese Entwicklung bekämpfen.<br>Dies können wir aber nicht allein.</p>
  </div>
  <h2 class="abs help">Wir benötigen Ihre HILFE!</h2>

  <div class="abs body col-mid">
    <p class="indent">Daher wird ein nicht unerheblicher Teil aus den<br>Einkünften der Patenschaften dazu verwendet Agrarflächen<br>umzugestalten für alle Bestäubenden Insekten. Flächen wer-<br>den Gepachtet oder gekauft und umgewidmet das sich die<br>natürlichen Populationen erholen können unter der Schirm-<br>herrschaft der Honigbiene. Wir haben im Jahr 2016 / 2017<br>bereits im Burgenland erste Flächen umgebaut und erste<br>Erfolge erzielt, wie im Umkreis dieser Flächen müssen auch<br>auf konventionellen Flächen weniger Insektizide eingesetzt<br>werden da die natürlichen Feinde dieser Insekten in diesen<br>Habitaten sich vermehrt haben und dies auf natürlichem<br>Wege reguliert haben. Da dies so gut funktioniert haben wir<br>beschlossen dieses Projekt ins Niederösterreich und Oberös-<br>terreich zu tragen und suchen daher noch nach unterstützen<br>für dieses Projekt.</p>
    <p class="indent gap">In Form einer Bienenpatenschaft um 290,00 schenken<br>Sie nicht nur 50.000 fleißigen Bienen (1 Bienenvolk) ein<br>neues Zuhause und ermöglichen diesen die notwendige<br>Pflege, um sicher durch das Jahr zu kommen. (Nahrung,<br>Behandlung gegen Schädlinge, Instandhaltung des Bienen-<br>stocks etc.) Sondern ermöglichen auch einen Grundstein für<br>die nächsten Projekte zu setzten.</p>
    <p>Die Patenschaft bringt Ihnen nicht nur die Gewissheit, Teil<br>eines guten Projekts zu sein. Sie ist natürlich auch fair und<br>funktioniert ganz einfach:</p>
  </div>

  <ul class="abs steps">
    <li><svg width="20" height="18" viewBox="0 0 20 18"><polygon points="5,0 15,0 20,9 15,18 5,18 0,9" fill="var(--gold)"/></svg>Bienenhof Seewinkel stellt Ihren<br>Bienenstock auf den Feldern des Biohofs auf.</li>
    <li><svg width="20" height="18" viewBox="0 0 20 18"><polygon points="5,0 15,0 20,9 15,18 5,18 0,9" fill="var(--gold)"/></svg>Bienenhof Seewinkel kümmert sich um<br>die Pflege und erntet den Honig.</li>
    <li><svg width="20" height="18" viewBox="0 0 20 18"><polygon points="5,0 15,0 20,9 15,18 5,18 0,9" fill="var(--gold)"/></svg>Bienenhof Seewinkel informiert Sie<br>über Leben und Arbeit Ihrer Bienen.</li>
    <li><svg width="20" height="18" viewBox="0 0 20 18"><polygon points="5,0 15,0 20,9 15,18 5,18 0,9" fill="var(--brown)"/></svg>Sie übernehmen die Patenschaft um<br>jährlich 290 Euro pro Bienenstock.</li>
    <li><svg width="20" height="18" viewBox="0 0 20 18"><polygon points="5,0 15,0 20,9 15,18 5,18 0,9" fill="var(--gold)"/></svg>Sie können Ihrem Bienenvolk und<br>Ihrer Königin einen Namen geben.</li>
    <li><svg width="20" height="18" viewBox="0 0 20 18"><polygon points="5,0 15,0 20,9 15,18 5,18 0,9" fill="var(--brown)"/></svg>Sie bekommen jährlich 6 kg Honig und<br>2 Flaschen Honigwein Ihres Bienenvolkes.</li>
  </ul>

  <h2 class="abs serif-head h-engage">Mit Ihrem<br>Engagement ...</h2>
  <p class="abs body col-right">... sichern Sie Tausenden dieser wundervollen Nützlinge<br>das Überleben und ermöglichen eine intensive und nach-<br>haltige Betreuung durch Ihren Imker. Mit einer Bienenpa-<br>tenschaft können Sie mit Stolz von sich behaupten, einen<br>messbaren Beitrag zum Überleben der Bienen, Erhalt der<br>Nahrungsmittelvielfalt und des Naturschutzes<br>geleistet zu haben.</p>
  <div class="abs rule"></div>
  <h2 class="abs serif-head h-project">Projekt SummWerk<br>Bienenmiete</h2>
  <p class="abs lead">Werde Imker auf Zeit und miete deinen eigenen<br>Bienenstock voller fleißiger Bestäuber.</p>
  <p class="abs body col-right2">Wollten Sie schon immer Imker werden und eigenen<br>Honig haben? Jetzt gibt es die Möglichkeit in die Imkerei<br>hinein zu schnuppern und einen Bienenstock für zwei<br>Monate <b>(190 Euro)</b> oder eine Saison <b>(290 Euro)</b> zu<br>„mieten“. Nach dieser Zeit gibt es den fix fertig abgefüllten<br>Honig „ihrer“ Bienen in 1-Kilo-Gläsern. „Alles was das<br>Bienenvolk im Honigraum sammelt gehört Ihnen“, und<br>kann an Ihre Liebsten und Freunde verschenkt werden.</p>
</main>
</body>
</html>
```